Maple Syrup Bottle (front) Label design

I need label design for a 16fl OZ rectangular bottle of maple syrup with the usable dimensions of: Front: 4" x 2" and the back area for "ingredient specifications" of: 6" x 2". The maple syrup product comes from our own farm and is a quality product. The technical name/class of the syrup is: Grade A / AMBER
Updates

I can’t seem to find a way to upload a photo of the maple syrup bottle, but the front dimensions are clearly written on bottle description. Again: 4.5” by 2.25”

I have tried to upload the photo of the maple syrup bottle several times, and it seems (from my side) that it is successful. But I can never find it and the artists cannot find it either. Not sure what to do.

I have tried several times to add a photo of maple bottle, but it never shows up

This seems to be a futile exercise

I would like to post some images of the actual cedar Hollow (not the one on Quorvo, though!
But I can’t get back to the page that allows that to happen. Please advise!

Somebody PLEASE ask PV management to make it possible for me to upload more images! The "add photos" etc. just disappears from anywhere.

Target Market(s)

High-end food stores

Industry/Entity Type

Maple syrup retail industry

Font styles to use
Other font styles liked:
• I don't know, and welcome suggestions

Colors

Designer to choose colors to be used in the design.

Requirements
Must have
• Name of Farm: Cedar Hollow Maple
Nice to have
• The label can be "minimalist" and elegant. There is already a Maple leaf glass relief on the top of front of the bottle.
Should not have
• and NOT include farm buildings with steam coming out the chimney, etc.

```html
<!DOCTYPE html>
<html lang="en">
<head>
<meta charset="utf-8">
<title>Cedar Hollow Maple — Maple Syrup Label</title>
<link rel="stylesheet" href="https://fonts.googleapis.com/css2?family=Bagel+Fat+One&family=Archivo+Black&family=Outfit:wght@300;400;600&display=swap">
<style>
  :root {
    --label-ground: #505050;
    --ink: #ffffff;
    --ink-soft: rgba(255, 255, 255, 0.92);
  }
  * { margin: 0; padding: 0; box-sizing: border-box; }
  html, body {
    width: 1200px;
    height: 2720px;
    overflow: hidden;
    background: var(--label-ground);
  }
  .label {
    width: 1200px;
    height: 2720px;
    display: flex;
    flex-direction: column;
    align-items: center;
    justify-content: center;
    color: var(--ink);
  }
  .brand {
    display: flex;
    align-items: center;
    gap: 26px;
  }
  .brand-dot {
    width: 56px;
    height: 56px;
    border-radius: 50%;
    border: 5px solid var(--ink);
  }
  .brand-name {
    font-family: "Archivo Black", sans-serif;
    font-size: 54px;
    letter-spacing: 4px;
    text-transform: uppercase;
    color: var(--ink);
  }
  .drip-line {
    display: block;
    margin: 40px 0 46px;
  }
  .product-name {
    font-family: "Bagel Fat One", sans-serif;
    font-size: 150px;
    line-height: 0.95;
    text-align: center;
    letter-spacing: 2px;
    text-transform: uppercase;
  }
  .drip-drop {
    display: block;
    margin: 46px 0 64px;
  }
  .grade {
    width: 640px;
    border-top: 4px solid var(--ink);
    border-bottom: 4px solid var(--ink);
    padding: 20px 0 18px;
    text-align: center;
    font-family: "Archivo Black", sans-serif;
    font-size: 40px;
    letter-spacing: 1px;
    text-transform: uppercase;
  }
  .claims {
    margin-top: 30px;
    font-family: "Outfit", sans-serif;
    font-weight: 400;
    font-size: 37px;
    color: var(--ink-soft);
  }
  .net-weight {
    margin-top: 44px;
    font-family: "Outfit", sans-serif;
    font-weight: 600;
    font-size: 37px;
    letter-spacing: 4px;
  }
</style>
</head>
<body>
  <main class="label">
    <div class="brand">
      <span class="brand-dot"></span>
      <span class="brand-name">Cedar Hollow Maple</span>
    </div>

    <svg class="drip-line" width="20" height="170" viewBox="0 0 20 170" aria-hidden="true">
      <path d="M10 0 C10 10 6 14 6 24 L6 170 L14 170 L14 24 C14 14 10 10 10 0 Z" fill="#ffffff"/>
    </svg>

    <h1 class="product-name">Maple<br>Syrup</h1>

    <svg class="drip-drop" width="24" height="90" viewBox="0 0 24 90" aria-hidden="true">
      <rect x="9" y="0" width="6" height="60" fill="#ffffff"/>
      <path d="M12 52 C17 62 21 68 21 76 A9 9 0 0 1 3 76 C3 68 7 62 12 52 Z" fill="#ffffff"/>
    </svg>

    <p class="grade">Grade A / Amber</p>
    <p class="claims">All Natural | No Additives | Gluten Free</p>
    <p class="net-weight">Net. Wt. 16Fl Oz</p>
  </main>
</body>
</html>
```